Web Design Project

need a website, logo and a matching business Card for design studio. i have a company that works with many companies and i want to offer design services that will be outsourced to drawfolk.

this website is totally for the design services. i need it to be simple but very catcgy and trendy, yet MUST BE ELEGENT.

you being a designer will know best what do i require in this website and how it should look and feel..

i dont need many pages, most of the selling work to clients will be face to face, this is just for them to view the sample works.

the company is called "Quenbrook, Artisan Studio", so pages i need are: 1- the Studio 2- Folios 3- Contact us( will include company informaiton, and online contact form that should have a drop-down list of all types of designs.

main focus is the folios pages, it needs to have samples of works, the classification of works should be on two basis, by type of design and by designer. client should be able to select a certain designer and send an inquiry. if the customer does that, then i should get all client details and the designer should get a notification that he has been requested though no contact details of client should be given to designer as i want to make sure that those jobs are given to designer through draw folk and this is an invitation for any designer who care to put his works on the website. next to that, if the customer requires a job online then we need to get information on how design should feel and look.

please quote your price to include the website and business card design, A3 head letter and envelope.

Please provide a mock up of your design or a briefing an initial design before asking to be announced as the winner.

Target Market(s)

my customers are general managers and decision makers.

Industry/Entity Type

Business

Requirements
Must have
• ability to filiter works based on type or designer. and website must offer all types of designs included here

```html
<!DOCTYPE html>
<html lang="en">
<head>
<meta charset="utf-8">
<title>Quenbrook Artisan Studio — The Studio</title>
<link rel="stylesheet" href="https://fonts.googleapis.com/css2?family=Arimo&family=Open+Sans:ital,wght@0,400;0,600;0,700;1,400&family=Oswald:wght@500&family=Playfair+Display:wght@800&family=Raleway:wght@100&display=swap">
<style>
  :root {
    --brand-blue: #7bafd4;
    --rule-blue: #cfe0ea;
    --tab-grey: #ededed;
    --tab-text: #9a9a9a;
    --ink: #333333;
    --ink-dark: #2e2e2e;
    --accent-red: #d42b2f;
    --accent-orange: #e8922e;
    --panel-grey: #efefef;
    --card-white: #ffffff;
    --card-border: #e2e2e2;
    --footer-bg: #262626;
    --footer-text: #a8a8a8;
    --link-orange: #e8761e;
  }
  * { box-sizing: border-box; margin: 0; padding: 0; }
  html, body { width: 1200px; height: 970px; overflow: hidden; background: #ffffff; }
  body { position: relative; font-family: "Open Sans", Arial, sans-serif; color: var(--ink); }

  .site-header { position: absolute; left: 0; top: 0; width: 1200px; height: 121px; border-bottom: 4px solid var(--rule-blue); background: #fff; }
  .brand { position: absolute; left: 42px; top: 12px; width: 184px; height: 100px; background: var(--brand-blue); color: #fff; font-family: "Open Sans", sans-serif; font-weight: 400; font-size: 25px; line-height: 29px; padding: 6px 0 0 12px; letter-spacing: 0.5px; }

  .main-nav { position: absolute; top: 67px; left: 469px; display: flex; gap: 4px; }
  .main-nav a { display: block; width: 225px; height: 45px; line-height: 45px; text-align: center; font-family: "Arimo", Arial, sans-serif; font-size: 20px; text-decoration: none; background: var(--tab-grey); color: var(--tab-text); }
  .main-nav a.is-active { background: var(--brand-blue); color: #fff; }

  .hero { position: absolute; left: 0; top: 121px; width: 1200px; height: 485px; background: #fff; }
  .hero-ring { position: absolute; left: 156px; top: 5px; }
  .tagline { position: absolute; left: 60px; top: 74px; }
  .tagline span { display: block; position: absolute; white-space: nowrap; }
  .tag-your { left: 0; top: 0; font-family: "Oswald", sans-serif; font-weight: 500; font-size: 42px; line-height: 40px; color: var(--ink-dark); }
  .tag-business { left: -3px; top: 30px; font-family: "Playfair Display", serif; font-weight: 800; font-size: 66px; line-height: 70px; color: var(--accent-red); letter-spacing: 1px; }
  .tag-our { left: 262px; top: 96px; font-family: "Oswald", sans-serif; font-weight: 500; font-size: 42px; line-height: 42px; color: var(--ink-dark); }
  .tag-creativity { left: 260px; top: 134px; font-family: "Raleway", sans-serif; font-weight: 100; font-size: 68px; line-height: 56px; color: var(--accent-red); letter-spacing: -2px; }
  .hero-cta { position: absolute; left: 210px; top: 379px; width: 220px; height: 42px; background: var(--accent-orange); color: #fff; font-family: "Raleway", sans-serif; font-size: 23px; line-height: 42px; padding-left: 16px; text-decoration: none; display: flex; align-items: center; gap: 10px; }
  .hero-art { position: absolute; left: 666px; top: 17px; width: 432px; height: 456px; border-radius: 46% 46% 8px 8px; background: radial-gradient(ellipse at 50% 35%, #e9e9e9 0%, #f3f3f3 55%, #ffffff 80%); }

  .services { position: absolute; left: 0; top: 606px; width: 1200px; height: 302px; background: var(--panel-grey); box-shadow: inset 0 6px 8px -6px rgba(0,0,0,0.15); }
  .carousel-arrow { position: absolute; top: 126px; width: 32px; height: 32px; background: #fff; display: flex; align-items: center; justify-content: center; }
  .carousel-arrow.prev { left: 42px; }
  .carousel-arrow.next { left: 1126px; }
  .service-card { position: absolute; top: 30px; width: 228px; height: 202px; background: var(--card-white); border: 1px solid var(--card-border); }
  .service-card h2 { font-weight: 400; font-size: 24px; color: var(--brand-blue); text-align: center; margin-top: 13px; }
  .price-badge { position: absolute; left: 14px; top: 73px; width: 116px; height: 116px; border-radius: 50%; background: radial-gradient(circle at 50% 40%, #ffffff 55%, #f4efe4 100%); box-shadow: 0 2px 5px rgba(0,0,0,0.18); text-align: center; }
  .price-badge .from { display: block; font-style: italic; font-size: 15px; color: #777; margin-top: 20px; }
  .price-badge .amount { display: block; font-weight: 700; font-size: 33px; color: var(--ink-dark); line-height: 38px; }
  .service-art { position: absolute; right: 8px; bottom: -14px; width: 86px; height: 78px; border-radius: 4px; }
  .learn-more { position: absolute; top: 260px; width: 104px; height: 21px; border-radius: 11px; background: linear-gradient(#fdfdfd, #e3e3e3); border: 1px solid #d0d0d0; font-family: "Arimo", Arial, sans-serif; font-size: 13px; line-height: 19px; text-align: center; color: #333; }

  .site-footer { position: absolute; left: 0; top: 908px; width: 1200px; height: 62px; background: var(--footer-bg); }
  .legal { position: absolute; left: 68px; top: 22px; font-size: 11.5px; color: var(--footer-text); }
  .legal a { color: var(--link-orange); text-decoration: none; }
  .social { position: absolute; left: 1014px; top: 10px; display: flex; align-items: center; gap: 1px; }
  .social-label { font-style: italic; font-size: 13px; color: var(--footer-text); margin-right: 14px; }
  .social-link { width: 38px; height: 38px; display: block; }
  .social-link.one { background: #5a86c6; }
  .social-link.two { background: #6ec3ea; }
</style>
</head>
<body>
  <header class="site-header">
    <div class="brand">QUENBROOK<br>ARTISAN<br>STUDIO</div>
    <nav class="main-nav">
      <a class="is-active" href="#studio">The Studio</a>
      <a href="#folios">Folios</a>
      <a href="#contact">Contact Us</a>
    </nav>
  </header>

  <section class="hero">
    <svg class="hero-ring" width="360" height="360" viewBox="0 0 360 360" aria-hidden="true">
      <circle cx="180" cy="180" r="178" fill="none" stroke="#b9b9b9" stroke-width="1.5" stroke-dasharray="4 4"/>
    </svg>
    <h1 class="tagline">
      <span class="tag-your">YOUR</span>
      <span class="tag-business">BUSINESS</span>
      <span class="tag-our">OUR</span>
      <span class="tag-creativity">CREATIVITY</span>
    </h1>
    <a class="hero-cta" href="#folios">View Our Folios
      <svg width="24" height="14" viewBox="0 0 24 14" aria-hidden="true"><path d="M1 7h21M16 1l6 6-6 6" fill="none" stroke="#fff" stroke-width="1.5"/></svg>
    </a>
    <div class="hero-art" role="img" aria-label="Illustration of a designer working at a desk with a cloud of creative icons rising above"></div>
  </section>

  <section class="services">
    <a class="carousel-arrow prev" href="#prev" aria-label="Previous">
      <svg width="10" height="16" viewBox="0 0 10 16"><path d="M8 1L2 8l6 7" fill="none" stroke="#222" stroke-width="1.5"/></svg>
    </a>

    <article class="service-card" style="left:109px">
      <h2>Logo Design</h2>
      <div class="price-badge"><span class="from">Starting at</span><span class="amount">$240</span></div>
      <div class="service-art" role="img" aria-label="Red paint splash mark" style="background:radial-gradient(circle,#d42b2f 45%,rgba(212,43,47,0) 70%)"></div>
    </article>
    <div class="learn-more" style="left:165px">Learn More</div>

    <article class="service-card" style="left:361px">
      <h2>Business Card</h2>
      <div class="price-badge"><span class="from">Starting at</span><span class="amount">$130</span></div>
      <div class="service-art" role="img" aria-label="Business card samples" style="background:linear-gradient(135deg,#f7f7f7,#e6e6e6)"></div>
    </article>
    <div class="learn-more" style="left:426px">Learn More</div>

    <article class="service-card" style="left:612px">
      <h2>Stationery</h2>
      <div class="price-badge"><span class="from">Starting at</span><span class="amount">$200</span></div>
      <div class="service-art" role="img" aria-label="Letterhead and envelope samples" style="background:linear-gradient(135deg,#f7f7f7,#e8e2d8)"></div>
    </article>
    <div class="learn-more" style="left:677px">Learn More</div>

    <article class="service-card" style="left:864px">
      <h2>Web Design</h2>
      <div class="price-badge"><span class="from">Starting at</span><span class="amount">$320</span></div>
      <div class="service-art" role="img" aria-label="Website screen sample" style="background:linear-gradient(135deg,#f3f3f3,#e0e4e8)"></div>
    </article>
    <div class="learn-more" style="left:929px">Learn More</div>

    <a class="carousel-arrow next" href="#next" aria-label="Next">
      <svg width="10" height="16" viewBox="0 0 10 16"><path d="M2 1l6 7-6 7" fill="none" stroke="#222" stroke-width="1.5"/></svg>
    </a>
  </section>

  <footer class="site-footer">
    <p class="legal">Copyright © 2012 Quenbrook Artisan Studio. Use of this website constitutes acceptance of our <a href="#">User Agreement</a>, <a href="#">Privacy Policy</a> and <a href="#">money back refund policy</a>.</p>
    <div class="social">
      <span class="social-label">Join Us</span>
      <a class="social-link one" href="#" aria-label="Social profile one"></a>
      <a class="social-link two" href="#" aria-label="Social profile two"></a>
    </div>
  </footer>
</body>
</html>
```